Interior Decoration and Concept Store needs a webpage design

Sophisticated website for my business, name Wren Hollow. Wren Hollow is a design service and homewares store run by interior decorator Marion Tulk.

Marion's qualification and work experience as an interior decorator, is able to provide advice and recommendations for interior and exterior concepts, colour consultations, furniture, lighting, decor concepts and products are sourced for individual projects. A re-upholstery service is also provided.

Friendsphere icon.
Projects page.
Profile page.
Established 2009
Medial page

Industry/Entity Type

Store

```html
<!DOCTYPE html>
<html lang="en">
<head>
<meta charset="utf-8">
<title>Wren Hollow — Interior Decoration &amp; Concept Store</title>
<link href="https://fonts.googleapis.com/css2?family=Lato:ital,wght@0,300;0,400;0,700;1,400&display=swap" rel="stylesheet">
<style>
:root{
  --ink:#3a3d42;
  --muted:#8a9aa8;
  --soft:#b7c0c8;
  --line:#e6e8ea;
  --white:#ffffff;
  --footer:#2b2e33;
  --footer-text:#a9aeb4;
  --caption:rgba(40,40,42,.82);
  --teal:#163f44;
}
*{box-sizing:border-box;margin:0;padding:0}
html,body{width:920px;height:1200px;overflow:hidden;background:var(--white)}
body{font-family:"Lato",sans-serif;color:var(--ink);position:relative}
.wrap{position:absolute;left:117px;width:686px}

.topbar{position:absolute;top:0;left:0;width:920px;height:28px;border-bottom:2px solid var(--line);font-size:8.5px;color:var(--ink)}
.topbar .est{position:absolute;left:121px;top:10px;font-style:italic;color:var(--soft)}
.topbar .contacts{position:absolute;left:202px;top:9px;display:flex;align-items:center;gap:16px;white-space:nowrap}
.topbar .contact{display:flex;align-items:center;gap:6px}
.topbar .social{position:absolute;right:108px;top:10px;display:flex;align-items:center;gap:4px}
.topbar .social i{display:block;width:7px;height:7px;background:var(--ink);border-radius:1px}

.header{position:absolute;top:30px;left:0;width:920px;height:64px}
.brand{position:absolute;left:117px;top:12px;font-size:27px;font-weight:300;letter-spacing:1px;color:var(--ink);display:flex;align-items:center;gap:8px}
.brand .dot{width:12px;height:12px;border-radius:50%;background:var(--ink)}
.nav{position:absolute;right:116px;top:25px;display:flex;gap:33px;font-size:10px;color:#5d6670}

.hero{position:absolute;top:94px;left:2px;width:916px;height:430px;
  background:linear-gradient(100deg,#c9a57a 0%,#d8c09d 24%,#ebe7e1 46%,#f3f2f0 70%,#ecebe8 100%)}
.caption{position:absolute;left:108px;top:173px;width:422px;height:185px;background:var(--caption);color:var(--white);padding:29px 34px 0}
.caption h1{font-weight:300;font-size:16px;white-space:nowrap;margin-bottom:12px}
.caption p{font-size:10px;line-height:16px;margin-bottom:15px;white-space:nowrap}
.caption .btn{display:inline-block;border:1.5px solid var(--white);padding:7px 15px;font-size:11px;font-weight:700}
.arrow{position:absolute;top:294px;width:29px;height:29px;background:#3b3f45}
.arrow svg{display:block;margin:10px auto}

h2{font-weight:300;font-size:21.5px;color:var(--ink)}
.welcome{top:555px;width:340px}
.portrait{position:absolute;top:43px;left:0;width:109px;height:109px;border-radius:50%;background:radial-gradient(circle at 50% 40%,#eeeeee,#c4c4c4)}
.person{position:absolute;left:119px;top:54px}
.person .name{font-size:13px}
.person .role{font-size:9px;color:var(--muted);margin-top:3px}
.person p{font-size:8.5px;line-height:14px;color:var(--muted);margin-top:9px;width:210px}

.services{top:555px;left:478px;width:330px}
.services .lead{font-size:8.5px;line-height:14px;color:var(--muted);margin-top:14px}
.services ul{list-style:none;display:grid;grid-template-columns:172px 150px;row-gap:11px;margin-top:14px;font-size:9px}
.services li{display:flex;align-items:center;gap:10px}
.services li i{width:13px;height:13px;border-radius:50%;background:#e4e7e9;display:flex;align-items:center;justify-content:center}

.projects-title{position:absolute;top:752px;left:0;width:920px;text-align:center}
.grid{position:absolute;top:793px;left:117px;width:686px;height:315px;display:grid;grid-template-columns:repeat(3,1fr);grid-template-rows:1fr 1fr;gap:1px;background:var(--white)}
.tile{position:relative}
.t1{background:linear-gradient(135deg,#8c7f6f,#d9d1c6 45%,#f1eee9)}
.t2{background:linear-gradient(160deg,#f2f1ee 0%,#e8e4da 55%,#8e7a25 100%)}
.t3{background:linear-gradient(180deg,#f3f1ee 0%,#ecdcc9 55%,#6b6661 100%)}
.t4{background:var(--teal);color:var(--white);text-align:center}
.t5{background:linear-gradient(135deg,#bfb6ab,#7f7a76 45%,#a07c5a 100%)}
.t6{background:linear-gradient(90deg,#f4f2ee 0%,#efe8da 50%,#8a4b2d 100%)}
.t4 svg{display:block;margin:35px auto 0}
.t4 .title{font-size:13px;margin-top:13px}
.t4 .sub{font-size:9px;margin-top:6px}

.footer{position:absolute;top:1159px;left:2px;width:916px;height:41px;background:var(--footer);color:var(--footer-text);font-size:10px}
.footer .copy{position:absolute;left:115px;top:15px}
.footer .nav{position:absolute;right:114px;top:15px;display:flex;gap:33px;color:var(--footer-text)}
</style>
</head>
<body>

<div class="topbar">
  <span class="est">Established 2009</span>
  <div class="contacts">
    <span class="contact">
      <svg width="21" height="10" viewBox="0 0 21 10"><rect x="9" y="1" width="11" height="8" fill="none" stroke="#3a3d42" stroke-width="1"/><path d="M9 1l5.5 4 5.5-4" fill="none" stroke="#3a3d42"/><path d="M1 3h6M3 6h4" stroke="#3a3d42"/></svg>
      hello@wrenhollow.com
    </span>
    <span class="contact">
      <svg width="11" height="11" viewBox="0 0 11 11"><path d="M2.5 1l2 2-1 1.2c.6 1.3 1.6 2.3 2.9 2.9l1.1-1 2 2-1.3 1.4C5 9 2 6 1.1 2.3z" fill="none" stroke="#3a3d42"/></svg>
      +1800 555 01234
    </span>
  </div>
  <span class="social"><i></i>Like us on Friendsphere</span>
</div>

<header class="header">
  <div class="brand"><span class="dot"></span>Wren Hollow</div>
  <nav class="nav"><span>Home</span><span>Projects</span><span>Profile</span><span>Medial</span><span>Contact</span></nav>
</header>

<section class="hero" role="img" aria-label="Bright living room photo with wooden cabinet, desk with laptop, chair and patterned cushions">
  <div class="caption">
    <h1>We Build Brands and Unique Style of Dedication</h1>
    <p>Quisque porttitor urna in felis luctus, nec congue libero lacinia.<br>Pellentesque habitant morbi tristique senectus et netus et malesuada fames<br>ac turpis egestas quisque porttitor</p>
    <span class="btn">READ MORE</span>
  </div>
  <div class="arrow" style="left:0"><svg width="6" height="9" viewBox="0 0 6 9"><path d="M5 1L1.5 4.5 5 8" fill="none" stroke="#fff" stroke-width="1.4"/></svg></div>
  <div class="arrow" style="right:0"><svg width="6" height="9" viewBox="0 0 6 9"><path d="M1 1l3.5 3.5L1 8" fill="none" stroke="#fff" stroke-width="1.4"/></svg></div>
</section>

<section class="wrap welcome">
  <h2>Welcome to Wren Hollow</h2>
  <div class="portrait" role="img" aria-label="Portrait photo of interior decorator Marion Tulk"></div>
  <div class="person">
    <div class="name">Marion Tulk</div>
    <div class="role">Interior Decorator</div>
    <p>Maecenas bibendum lacus gravida placerat consequat. Vivamus quis hendrerit mauris. Vestibulum laoreet felis sed consectetur sollicitudin.</p>
  </div>
</section>

<section class="wrap services">
  <h2>Our Services</h2>
  <p class="lead">Maecenas bibendum lacus gravida placerat consequat. Vivamus quis hendrerit mauris. Vestibulum laoreet felis sed consectetur sollicitudin.</p>
  <ul>
    <li><i><svg width="5" height="7" viewBox="0 0 5 7"><path d="M1 1l2.5 2.5L1 6" fill="none" stroke="#fff" stroke-width="1.2"/></svg></i>Interior and exterior concepts</li>
    <li><i><svg width="5" height="7" viewBox="0 0 5 7"><path d="M1 1l2.5 2.5L1 6" fill="none" stroke="#fff" stroke-width="1.2"/></svg></i>Lighting</li>
    <li><i><svg width="5" height="7" viewBox="0 0 5 7"><path d="M1 1l2.5 2.5L1 6" fill="none" stroke="#fff" stroke-width="1.2"/></svg></i>Colour consultations</li>
    <li><i><svg width="5" height="7" viewBox="0 0 5 7"><path d="M1 1l2.5 2.5L1 6" fill="none" stroke="#fff" stroke-width="1.2"/></svg></i>Decor concepts and products</li>
    <li><i><svg width="5" height="7" viewBox="0 0 5 7"><path d="M1 1l2.5 2.5L1 6" fill="none" stroke="#fff" stroke-width="1.2"/></svg></i>Furniture</li>
    <li><i><svg width="5" height="7" viewBox="0 0 5 7"><path d="M1 1l2.5 2.5L1 6" fill="none" stroke="#fff" stroke-width="1.2"/></svg></i>Re-upholstery services</li>
  </ul>
</section>

<h2 class="projects-title">Our Projects</h2>
<section class="grid">
  <div class="tile t1" role="img" aria-label="Upholstered armchair with woven cushion"></div>
  <div class="tile t2" role="img" aria-label="Olive green mid-century armchair beside white shelf"></div>
  <div class="tile t3" role="img" aria-label="Glass vase and bowl on a dark sideboard"></div>
  <div class="tile t4" role="img" aria-label="Dark teal cabinet with project overlay">
    <svg width="32" height="32" viewBox="0 0 32 32"><circle cx="16" cy="16" r="14.5" fill="none" stroke="#fff" stroke-width="2"/><path d="M16 8v16M8 16h16" stroke="#fff" stroke-width="2"/></svg>
    <div class="title">Awesome Project Title</div>
    <div class="sub">Interior Design</div>
  </div>
  <div class="tile t5" role="img" aria-label="Sofa with metal side table on timber floor"></div>
  <div class="tile t6" role="img" aria-label="White console with yellow bowl beside polished timber floor"></div>
</section>

<footer class="footer">
  <span class="copy">Copyright © 2014 - Wren Hollow</span>
  <nav class="nav"><span>Home</span><span>Projects</span><span>Profile</span><span>Medial</span><span>Contact</span></nav>
</footer>

</body>
</html>
```